Law Firm Needs a Stationery Design

We need a stationery design for a law firm based in the East African region called 'Mbweteka Olinyo & Company Advocates'. We are a law firm specializing in commercial, public and constitutional law. Our practice areas include Telecommunications Law, Mining Law, Oil and Energy Law, Real Estate and Land Development Law, Employment Law, Family Law, Civil and Criminal Litigation, Constitutional Law, Company Secretariat and more. We represent a wide variety of clients, ranging from individuals to corporations and approach each case with full attention, dedication and legal acumen in order to protect the interests of our clients. The final stationary design should communicate innovation and expertise to meet our clients’ legal needs.
Target Market(s)
New clients, current and former clients, other lawyers in and outside of our practice area, or other professionals, contacts and centers of influence within the region
Industry/Entity Type
Real Estate
Colors
Designer to choose colors to be used in the design.
Look and feel
Each slider illustrates characteristics of the customer's brand and the style your logo design should communicate.

```html
<!DOCTYPE html>
<html lang="en">
<head>
<meta charset="utf-8">
<title>Mbweteka Olinyo &amp; Company Advocates — Stationery</title>
<link href="https://fonts.googleapis.com/css2?family=Cabin:wght@400&family=PT+Sans:wght@400&family=Italianno&display=swap" rel="stylesheet">
<style>
  :root {
    --brand-orange: #e3a02f;
    --ink: #4a4a4c;
    --ink-soft: #6b6b6d;
    --paper: #ffffff;
    --edge: #b9b9b9;
    --band-dark: #58585a;
    --band-end: #6a6f6f;
    --band: linear-gradient(90deg, var(--band-dark) 0%, #7a7063 30%, var(--brand-orange) 50%, #85796a 68%, var(--band-end) 100%);
  }
  * { box-sizing: border-box; margin: 0; padding: 0; }
  html, body { width: 1200px; height: 810px; overflow: hidden; background: var(--paper); }
  .canvas { position: relative; width: 1200px; height: 810px; font-family: "Cabin", sans-serif; color: var(--ink); }

  .sheet { position: absolute; background: var(--paper); border: 1px solid var(--edge); overflow: hidden; }
  .band { position: absolute; left: 0; right: 0; bottom: 0; background: var(--band); }

  .mark { position: absolute; width: 30px; height: 30px; background: var(--brand-orange); }
  .firm-name { position: absolute; font-family: "PT Sans", sans-serif; font-size: 11px; color: var(--ink); letter-spacing: 0.2px; line-height: 1; white-space: nowrap; }
  .firm-sub { position: absolute; font-family: "Cabin", sans-serif; font-size: 7.5px; color: var(--ink-soft); letter-spacing: 0.6px; line-height: 1; white-space: nowrap; }
  .rule { position: absolute; height: 2px; background: var(--brand-orange); }
  .contact { position: absolute; text-align: right; font-size: 6.4px; line-height: 8.3px; color: var(--ink); letter-spacing: 0.4px; }

  /* Letterhead */
  .letterhead { left: 27px; top: 24px; width: 529px; height: 747px; }
  .letterhead .band { height: 28px; }

  /* Business card */
  .card-front { left: 583px; top: 36px; width: 229px; height: 139px; }
  .card-front .band { height: 19px; }
  .card-back { left: 832px; top: 36px; width: 229px; height: 139px; }
  .card-back .person { position: absolute; left: 19px; top: 28px; font-size: 11px; letter-spacing: 0.6px; color: var(--ink); }
  .card-back .role { position: absolute; left: 19px; top: 41px; font-size: 7.5px; color: var(--ink-soft); letter-spacing: 0.4px; }
  .card-back .details { position: absolute; left: 19px; top: 57px; font-size: 8px; line-height: 10px; letter-spacing: 0.5px; color: var(--ink); }
  .card-back .details p { margin-bottom: 3px; }

  /* Compliments slip */
  .comp-slip { left: 576px; top: 196px; width: 531px; height: 226px; }
  .comp-slip .band { height: 22px; }
  .comp-slip .sign-off { position: absolute; right: 8px; top: 170px; font-family: "Italianno", cursive; font-size: 26px; color: var(--ink); }

  /* Envelope */
  .envelope { left: 578px; top: 469px; width: 585px; height: 234px; }
  .envelope .address-line { position: absolute; left: 22px; font-size: 5.6px; letter-spacing: 0.4px; color: var(--ink); }
  .envelope .window { position: absolute; left: 71px; top: 131px; width: 257px; height: 68px; border: 1px solid var(--edge); border-radius: 7px; }
</style>
</head>
<body>
<main class="canvas">

  <section class="sheet letterhead" aria-label="Letterhead">
    <div class="mark" style="left:51px; top:40px; width:40px; height:40px;"></div>
    <div class="rule" style="left:88px; right:13px; top:91px;"></div>
    <div class="firm-name" style="left:13px; top:99px;">MBWETEKA OLINYO</div>
    <div class="firm-sub" style="left:27px; top:111px;">&amp; Company Advocates</div>
    <address class="contact" style="right:17px; top:42px; font-style:normal;">
      Plot 7-9 Nsonga Close,<br>Lumuli, Kampala, Uganda<br>+256 300 418 562<br>info@mbwetekaolinyo.com<br>www.mbwetekaolinyo.com
    </address>
    <div class="band"></div>
  </section>

  <section class="sheet card-front" aria-label="Business card, front">
    <div class="mark" style="left:98px; top:16px; width:34px; height:34px;"></div>
    <div class="firm-name" style="left:0; right:0; top:66px; text-align:center;">MBWETEKA OLINYO</div>
    <div class="firm-sub" style="left:0; right:0; top:78px; text-align:center;">&amp; Company Advocates</div>
    <div class="band"></div>
  </section>

  <section class="sheet card-back" aria-label="Business card, back">
    <div class="person">Name Surname</div>
    <div class="role">Role</div>
    <div class="details">
      <p>Plot 7-9 Nsonga Close,<br>Lumuli, Kampala, Uganda</p>
      <p>+256 300 418 562</p>
      <p>info@mbwetekaolinyo.com</p>
      <p>www.mbwetekaolinyo.com</p>
    </div>
  </section>

  <section class="sheet comp-slip" aria-label="Compliments slip">
    <div class="mark" style="left:36px; top:13px; width:36px; height:36px;"></div>
    <div class="rule" style="left:104px; right:8px; top:69px;"></div>
    <div class="firm-name" style="left:13px; top:77px; font-size:10px;">MBWETEKA OLINYO</div>
    <div class="firm-sub" style="left:26px; top:88px; font-size:7px;">&amp; Company Advocates</div>
    <address class="contact" style="right:9px; top:28px; font-style:normal;">
      Plot 7-9 Nsonga Close,<br>Lumuli, Kampala, Uganda<br>+256 300 418 562<br>info@mbwetekaolinyo.com<br>www.mbwetekaolinyo.com
    </address>
    <div class="sign-off">with compliments</div>
    <div class="band"></div>
  </section>

  <section class="sheet envelope" aria-label="Envelope">
    <div class="mark" style="left:42px; top:9px; width:30px; height:30px;"></div>
    <div class="firm-name" style="left:22px; top:58px; font-size:8.5px;">MBWETEKA OLINYO</div>
    <div class="firm-sub" style="left:33px; top:67px; font-size:6px;">&amp; Company Advocates</div>
    <div class="address-line" style="top:78px;">Plot 7-9 Nsonga Close, Lumuli, Kampala, Uganda</div>
    <div class="address-line" style="top:86px;">www.mbwetekaolinyo.com</div>
    <div class="window"></div>
  </section>

</main>
</body>
</html>
```